Design for a facebook fanpage COVER

I want a design for my facebook fanpage COVER,

It is an entretainmnt and vídeos fanpage on facebook, we want something funny but nice.

You can see our logo (on profile picture) for an idea. We want something that matches.

https://www.pagebook.example/LasRisasBrillantes

THANK YOU AND GOOD LUCK!

```html
<!DOCTYPE html>
<html lang="es">
<head>
<meta charset="utf-8">
<title>Risas Brillantes – Portada</title>
<link href="https://fonts.googleapis.com/css2?family=Itim&family=Satisfy&display=swap" rel="stylesheet">
<style>
  :root {
    --space-deep: #1a0c3a;
    --space-violet: #6a2fa8;
    --space-pink: #e24fb8;
    --space-glow: #f7c6ff;
    --strip-black: #141014;
    --strip-hole: #f4f0f4;
    --title-fill: rgba(120, 150, 205, 0.55);
    --title-edge: #3a2a5c;
    --link-ink: #3b1408;
    --link-edge: #f59ac8;
    --face-yellow: #f6c23c;
    --face-pink: #d8329c;
    --face-ring: #4a1050;
    --frame-tone-a: #c9a58e;
    --frame-tone-b: #9a8c8a;
  }
  html, body {
    margin: 0;
    padding: 0;
    width: 1200px;
    height: 445px;
    overflow: hidden;
    background: var(--space-deep);
  }
  .cover {
    position: relative;
    width: 1200px;
    height: 445px;
    overflow: hidden;
  }
  .cover svg { display: block; }
  .title-word {
    font-family: "Itim", "Comic Sans MS", sans-serif;
    fill: var(--title-fill);
    stroke: var(--title-edge);
    stroke-width: 2.5;
    paint-order: stroke;
  }
  .page-link {
    font-family: "Satisfy", cursive;
    font-weight: 400;
    fill: var(--link-ink);
    stroke: var(--link-edge);
    stroke-width: 2.5;
    paint-order: stroke;
  }
</style>
</head>
<body>
<div class="cover">
  <svg width="1200" height="445" viewBox="0 0 1200 445" xmlns="http://www.w3.org/2000/svg">
    <defs>
      <radialGradient id="space-burst" cx="0.55" cy="0.45" r="0.7">
        <stop offset="0" stop-color="var(--space-glow)"/>
        <stop offset="0.25" stop-color="var(--space-pink)"/>
        <stop offset="0.6" stop-color="var(--space-violet)"/>
        <stop offset="1" stop-color="var(--space-deep)"/>
      </radialGradient>
      <radialGradient id="face-tone" cx="0.5" cy="0.35" r="0.7">
        <stop offset="0" stop-color="var(--face-yellow)"/>
        <stop offset="0.55" stop-color="#f08a7a"/>
        <stop offset="1" stop-color="var(--face-pink)"/>
      </radialGradient>
      <pattern id="strip-holes" width="20" height="24" patternUnits="userSpaceOnUse">
        <rect x="4" y="6" width="11" height="13" rx="2" fill="var(--strip-hole)"/>
      </pattern>
    </defs>

    <!-- backdrop -->
    <rect class="space-backdrop" role="img" aria-label="Fondo de galaxia violeta y rosa con destellos de luz" width="1200" height="445" fill="url(#space-burst)"/>

    <!-- central mascot area -->
    <g class="mascot" role="img" aria-label="Mascota sonriente amarilla y rosa">
      <circle cx="663" cy="212" r="205" fill="url(#face-tone)" stroke="var(--face-ring)" stroke-width="12" opacity="0.85"/>
    </g>

    <!-- left film strip -->
    <g class="film-strip film-strip--left">
      <rect x="0" y="0" width="134" height="445" fill="var(--strip-black)"/>
      <rect x="0" y="0" width="22" height="445" fill="url(#strip-holes)"/>
      <rect x="112" y="0" width="22" height="445" fill="url(#strip-holes)"/>
      <rect class="film-frame" role="img" aria-label="Foto de un bebé" x="28" y="6" width="78" height="94" fill="var(--frame-tone-a)"/>
      <rect class="film-frame" role="img" aria-label="Foto de un bebé sonriendo" x="28" y="118" width="78" height="94" fill="#d8b9a0"/>
      <rect class="film-frame" role="img" aria-label="Foto de un actor haciendo una mueca" x="28" y="228" width="78" height="94" fill="#a88a70"/>
      <rect class="film-frame" role="img" aria-label="Dibujo de una cara riendo" x="28" y="338" width="78" height="94" fill="#e8e4e4"/>
    </g>

    <!-- right film strip -->
    <g class="film-strip film-strip--right">
      <rect x="1056" y="0" width="144" height="445" fill="var(--strip-black)"/>
      <rect x="1056" y="0" width="22" height="445" fill="url(#strip-holes)"/>
      <rect x="1178" y="0" width="22" height="445" fill="url(#strip-holes)"/>
      <rect class="film-frame" role="img" aria-label="Foto de un gato sorprendido" x="1088" y="6" width="82" height="112" fill="var(--frame-tone-b)"/>
      <rect class="film-frame" role="img" aria-label="Foto de un hombre sonriendo" x="1088" y="136" width="82" height="112" fill="#8a6a5a"/>
      <rect class="film-frame" role="img" aria-label="Foto en blanco y negro de una cara graciosa" x="1088" y="266" width="82" height="112" fill="#b8b4b4"/>
      <rect class="film-frame" role="img" aria-label="Dibujo de una cara burlona" x="1088" y="396" width="82" height="49" fill="#ece8ec"/>
    </g>

    <!-- titles -->
    <text class="title-word" x="582" y="128" font-size="132" text-anchor="middle">Risas</text>
    <text class="title-word" x="590" y="362" font-size="124" text-anchor="middle" textLength="920" lengthAdjust="spacingAndGlyphs">Brillantes</text>

    <!-- page link -->
    <text class="page-link" x="158" y="122" font-size="40" transform="rotate(8.4 158 122)" textLength="880" lengthAdjust="spacingAndGlyphs">https://www.pagebook.example/LasRisasBrillantes</text>
  </svg>
</div>
</body>
</html>
```